Certificate of Completion - Educational Trainings

We are looking for a certificate of completion for individuals who complete one of our specific trainings. Files should be provided in a Word (docx) or PowerPoint (pptx) format. The "Halvorcrest example.png" file is to show necessary information. Copies of logos have been included for design purposes.

Target Market(s)

Training Participants

Industry/Entity Type

Healthcare

Font styles to use
Sans Serif

```html
<!DOCTYPE html>
<html lang="en">
<head>
<meta charset="utf-8">
<title>Halvorcrest Certificate of Completion</title>
<link href="https://fonts.googleapis.com/css2?family=Lato:wght@300;400;700;900&family=Great+Vibes&display=swap" rel="stylesheet">
<style>
  :root {
    --page-bg: #9a9a9a;
    --green-light: #1d6a4c;
    --green-deep: #0a3a24;
    --green-band: #0b3a22;
    --paper: #f4f4f4;
    --ink: #161616;
    --ink-soft: #3a3a3a;
    --white: #ffffff;
    --script-green: #52a64b;
    --gold-1: #f6ea4a;
    --gold-2: #f3e38a;
    --gold-3: #b87a2c;
    --gold-4: #f7b62a;
    --gold-5: #ffd52a;
    --rule: #2f8a5a;
  }
  * { margin: 0; padding: 0; box-sizing: border-box; }
  html, body { width: 1200px; height: 904px; overflow: hidden; background: var(--page-bg); }
  .certificate {
    position: absolute; left: 0; top: 27px; width: 1200px; height: 849px; overflow: hidden;
    background: radial-gradient(ellipse 70% 80% at 50% 35%, var(--green-light) 0%, #155a3e 45%, var(--green-deep) 100%);
    font-family: "Lato", sans-serif; color: var(--white); text-align: center;
  }
  .header-arc { position: absolute; left: 0; top: 0; width: 1200px; height: 240px; }
  .brand-name {
    position: absolute; top: 40px; left: 0; width: 100%;
    font-weight: 900; font-size: 42px; letter-spacing: 2px; color: var(--ink); text-transform: uppercase;
  }
  .sponsor-details {
    position: absolute; top: 99px; left: 0; width: 100%;
    font-size: 14px; line-height: 19px; letter-spacing: 0.6px; color: var(--ink-soft); text-transform: uppercase;
  }
  .title-main {
    position: absolute; top: 250px; left: 0; width: 100%;
    font-weight: 700; font-size: 108px; line-height: 1; letter-spacing: 3px;
    background: linear-gradient(90deg, var(--gold-1) 22%, var(--gold-2) 38%, var(--gold-3) 52%, var(--gold-4) 66%, var(--gold-5) 80%);
    -webkit-background-clip: text; background-clip: text; color: transparent;
  }
  .title-sub {
    position: absolute; top: 355px; left: 0; width: 100%;
    font-weight: 700; font-size: 51px; line-height: 1; letter-spacing: 2px;
  }
  .awarded-label {
    position: absolute; top: 462px; left: 0; width: 100%;
    font-weight: 700; font-size: 22px; letter-spacing: 1.4px;
  }
  .recipient-name {
    position: absolute; top: 500px; left: 0; width: 100%;
    font-family: "Great Vibes", cursive; font-size: 62px; line-height: 1; color: var(--script-green);
  }
  .recipient-rule {
    position: absolute; top: 567px; left: 291px; width: 632px;
    border-top: 3px dotted #0a2a1a;
  }
  .course-details {
    position: absolute; top: 582px; left: 0; width: 100%;
    font-weight: 300; font-size: 17.5px; line-height: 25px; letter-spacing: 0.5px; color: #e9f0ec;
  }
  .signoff { position: absolute; top: 712px; width: 210px; }
  .signoff--date { left: 161px; }
  .signoff--signer { left: 818px; }
  .signoff-value {
    font-family: "Great Vibes", cursive; font-size: 28px; line-height: 36px; height: 40px;
  }
  .signoff--date .signoff-value { font-family: "Lato", sans-serif; font-style: italic; font-weight: 300; font-size: 22px; }
  .signoff-rule { border-top: 1px dashed var(--rule); margin: 4px 0 14px; }
  .signoff-label { font-size: 16px; letter-spacing: 1px; text-transform: uppercase; }
</style>
</head>
<body>
<main class="certificate">
  <svg class="header-arc" viewBox="0 0 1200 240" aria-hidden="true">
    <defs>
      <linearGradient id="goldBand" x1="0" x2="1" y1="0" y2="0">
        <stop offset="0" stop-color="#f6e94a"/>
        <stop offset="0.3" stop-color="#f2e08a"/>
        <stop offset="0.5" stop-color="#b9792b"/>
        <stop offset="0.75" stop-color="#f7b62a"/>
        <stop offset="1" stop-color="#ffd726"/>
      </linearGradient>
    </defs>
    <path d="M44 0 Q600 452 1156 0 Z" fill="url(#goldBand)"/>
    <path d="M52 0 Q600 406 1148 0 Z" fill="var(--green-band)"/>
    <path d="M60 0 Q600 322 1140 0 Z" fill="var(--paper)"/>
  </svg>

  <div class="brand-name">Halvorcrest</div>
  <p class="sponsor-details">48 Harbor Lane, Ste. 310 Brookfield, ME 04920<br>National Registry Sponsor Number 58213</p>

  <h1 class="title-main">CERTIFICATE</h1>
  <h2 class="title-sub">OF COMPLETION</h2>

  <p class="awarded-label">THIS CERTIFICATE IS AWARDED TO</p>
  <p class="recipient-name">Daniel Whitcombe</p>
  <div class="recipient-rule"></div>

  <p class="course-details">
    For successful completion of<br>
    Best Practices: Budget Process/Budget Building<br>
    Completed Online Field of Study Finance<br>
    CPE Credits: 1
  </p>

  <div class="signoff signoff--date">
    <div class="signoff-value">05/16/2025</div>
    <div class="signoff-rule"></div>
    <div class="signoff-label">Completion Date</div>
  </div>
  <div class="signoff signoff--signer">
    <div class="signoff-value">Laura Menden</div>
    <div class="signoff-rule"></div>
    <div class="signoff-label">Senior Consultant</div>
  </div>
</main>
</body>
</html>
```